GVA Business Card

I would like to create a busienss card for the high school teachers. Our school colors are red and black and our mascot is the bulldog. In addition, to our school address and contact information, I would like to add our twitter account and fb account. We also have a school website. Somewhere I would like to incorporate our school wide expectations: Be Safe, Be Respectful, Be Responsible and Be a Learner.

Tillbrook High School
2424 Fernwick
Tillbrook, KS 67193
785.904.2718
785.904.2719(fax)
www.tillbrookacademies.org
www.facebook.com/TillbrookHornets
twitter.com/TillbrookKsDST or @TillbrookKsDST
Teacher Name:
Teacher Email:

I would like to personalize each card with the teacher name and their email.

I would also like to use Hornet Circle – Roots.Now.Ahead

                                      Front Side of Card:  Teacher and School Contact Information

Back Side of Card:  Hornet Circle -several designers have asked about this-our school is trying to promote that we are a family trying to promote a positive climate.  We also want to add Roots.Now.Ahead with information that might pertain to the past, present, or future to keep people coming back to our website or facebook.

At first I mentioned that I wanted to use the bulldog as the graphic because it is our mascot, now I am changing my mind about maybe something more student centered like a group of stick figures circle together or arms around each other symbolizing that we are working together to accomplish our goal.

I need to make sure that our school wide expectations are also incorporated:

Be Safe.Be Respectful.Be Responsible.Be A Learner

Target Market(s)

9-12 students and professionals

Industry/Entity Type

High School

Requirements
Must have
• Contact information
Hornet Circle with Roots, Now and Ahead Incorporated
Two sided business card
Side #1 Contact Info + graphic (might use bulldog that I attached however not sure if I like it)
Side #2 Hornet Circle with Roots, Now and Ahead (incorporate a graphic that symbolizes togetherness or working together.

```html
<!DOCTYPE html>
<html lang="en">
<head>
<meta charset="utf-8">
<title>Tillbrook High School – Teacher Business Card</title>
<link rel="stylesheet" href="https://fonts.googleapis.com/css2?family=Montserrat:wght@700;800&family=Arimo:wght@400;700&display=swap">
<style>
  :root {
    --stage: #2b2b2b;
    --card: #f7f7f6;
    --red: #a8191e;
    --ink: #2a2a2a;
    --ink-soft: #444444;
    --figure-light: #e4e4e4;
    --figure-mid: #bdbdbd;
  }
  * { box-sizing: border-box; margin: 0; padding: 0; }
  html, body {
    width: 1200px;
    height: 900px;
    overflow: hidden;
  }
  body {
    background: var(--stage);
    font-family: "Arimo", Arial, sans-serif;
    color: var(--ink);
    position: relative;
  }
  .card {
    position: absolute;
    top: 307px;
    width: 500px;
    height: 286px;
    background: var(--card);
    border-radius: 28px;
    overflow: hidden;
  }
  .card--back { left: 70px; }
  .card--front { left: 630px; }

  /* Back side: togetherness graphic + motto */
  .togetherness-graphic {
    position: absolute;
    left: 0; top: 0;
    width: 100%;
    height: 200px;
    background: radial-gradient(ellipse at 55% 55%, var(--figure-mid) 0%, var(--figure-light) 55%, var(--card) 85%);
  }
  .motto {
    position: absolute;
    left: 0; right: 0;
    top: 212px;
    text-align: center;
    font-family: "Montserrat", Arial, sans-serif;
    font-weight: 700;
    font-size: 23px;
    color: var(--red);
    letter-spacing: -0.2px;
  }
  .social-links {
    position: absolute;
    left: 0; right: 0;
    top: 250px;
    text-align: center;
    font-size: 13px;
    color: var(--ink);
  }
  .social-links .divider { margin: 0 6px; }

  /* Front side: school + teacher contact */
  .school-name {
    position: absolute;
    left: 38px;
    top: 32px;
    font-family: "Montserrat", Arial, sans-serif;
    font-weight: 800;
    color: var(--red);
    text-transform: uppercase;
    line-height: 1;
  }
  .school-name__main { display: block; font-size: 22px; letter-spacing: 0.3px; }
  .school-name__sub { display: block; font-size: 17px; margin-top: 1px; }
  .expectations {
    position: absolute;
    left: 38px;
    top: 82px;
    font-size: 15.5px;
    color: var(--ink);
    white-space: nowrap;
  }
  .teacher {
    position: absolute;
    left: 38px;
    top: 122px;
  }
  .teacher__name {
    font-family: "Montserrat", Arial, sans-serif;
    font-weight: 700;
    font-size: 17px;
    color: var(--red);
    text-transform: uppercase;
  }
  .teacher__email { font-size: 13px; margin-top: 1px; }
  .school-address {
    position: absolute;
    left: 38px;
    top: 178px;
    font-style: normal;
    font-size: 13px;
    line-height: 1.5;
    color: var(--ink-soft);
  }
  .school-contact {
    position: absolute;
    left: 275px;
    top: 188px;
    font-size: 13px;
    line-height: 1.5;
    color: var(--ink);
  }
  .school-contact strong { font-weight: 700; }
  .accent-band {
    position: absolute;
    left: 0; right: 0; bottom: 0;
    height: 20px;
    background: var(--red);
  }
</style>
</head>
<body>

  <section class="card card--back" aria-label="Card back">
    <div class="togetherness-graphic" role="img" aria-label="Paper cut-out figures of students and families holding hands in a circle"></div>
    <h2 class="motto">Roots, Now and Ahead</h2>
    <p class="social-links">
      <span>www.facebook.com/TillbrookHornets</span><span class="divider">//</span><span>@TillbrookKsDST</span>
    </p>
  </section>

  <section class="card card--front" aria-label="Card front">
    <h1 class="school-name">
      <span class="school-name__main">Tillbrook</span>
      <span class="school-name__sub">High School</span>
    </h1>
    <p class="expectations">Be Safe.Be Respectful.Be Responsible.Be a Learner</p>
    <div class="teacher">
      <p class="teacher__name">Rhea Calloway</p>
      <p class="teacher__email">rcalloway@postvale.com</p>
    </div>
    <address class="school-address">
      Tillbrook High School<br>
      2424 Fernwick<br>
      Tillbrook, KS 67193
    </address>
    <p class="school-contact">
      Phone: 785.904.2718<br>
      Fax: 785.904.2719<br>
      www.<strong>tillbrookacademies</strong>.org
    </p>
    <div class="accent-band"></div>
  </section>

</body>
</html>
```